RLT PowerPoint

I am looking for a clean, corporate PowerPoint template.

I would like the following:
- title slide
- break slide
- blank slide with title (for graphs or graphics)
- an ending slide.

Target Market(s)

Business professionals, medium to large business clients.

Requirements
Must have
• Must incorporate the RLT logo in either the header or footer

```html
<!DOCTYPE html>
<html lang="en">
<head>
<meta charset="utf-8">
<title>RLT – Ending Slide</title>
<link rel="stylesheet" href="https://fonts.googleapis.com/css2?family=Source+Sans+3:wght@400;600&display=swap">
<style>
  :root {
    --brand-blue: #0055a5;
    --footer-grey: #ebebeb;
    --text-light: #ffffff;
    --logo-blue: #0a58a8;
  }
  * { margin: 0; padding: 0; box-sizing: border-box; }
  html, body {
    width: 1200px;
    height: 875px;
    overflow: hidden;
    background: var(--footer-grey);
    font-family: "Source Sans 3", "Myriad Pro", Arial, sans-serif;
  }
  .slide {
    position: relative;
    width: 1200px;
    height: 875px;
  }
  .contact-panel {
    position: absolute;
    left: 0;
    top: 0;
    width: 1200px;
    height: 710px;
    background: var(--brand-blue);
    color: var(--text-light);
  }
  .contact-details {
    position: absolute;
    left: 26px;
    top: 455px;
    list-style: none;
    font-size: 20px;
    line-height: 36px;
  }
  .company-summary {
    position: absolute;
    left: 26px;
    top: 634px;
    width: 1150px;
    font-size: 15.5px;
    line-height: 21px;
  }
  .footer-band {
    position: absolute;
    left: 0;
    top: 710px;
    width: 1200px;
    height: 165px;
    background: var(--footer-grey);
  }
  .brand-name {
    position: absolute;
    right: 40px;
    top: 56px;
    display: flex;
    align-items: center;
    gap: 14px;
    color: var(--logo-blue);
    font-size: 40px;
    font-weight: 600;
    letter-spacing: 0.5px;
  }
  .brand-square {
    width: 26px;
    height: 26px;
    background: var(--logo-blue);
  }
</style>
</head>
<body>
<main class="slide">
  <section class="contact-panel">
    <ul class="contact-details">
      <li>Reid Lowe Advisory Pty Ltd / 48 702 915 366</li>
      <li>PO Box 412, Kingsford Bay TASMANIA 7104</li>
      <li>+61 (0) 400 555 218</li>
      <li>reid@reidloweadvisory.com</li>
    </ul>
    <p class="company-summary">RLT is an independent contracting and consulting company that specialises in providing strategic advice and operational support to organisations utilising, adopting or expanding use of LedgerWorks solutions.</p>
  </section>
  <footer class="footer-band">
    <div class="brand-name">
      <span class="brand-square"></span>
      <span>RLT Reid Lowe Advisory</span>
    </div>
  </footer>
</main>
</body>
</html>
```